Need a Revamped Website - WaveCrestline.com

I am looking for a website designed for www.wavecrestline.com
The present website has content relating to the Kabwe Airwave Gathering - an annual meeting for radio practitioners in Zambia. My intention is to change the focus: to make the website a resource hub for radio practitioners in Africa. The site is to have the following:
Featured articles (opinion pieces) contributed by industry insiders.
Links to various radio stations websites
An events calendar focusing on radio related events
News (radio industry updates) etc
The site should also be able to incorporate social media mechanisms such as 'Likes' through to Facebook or articles to be shared on Twitter etc.
The focus of the word Summit, for the purposes of the website, should shift. Instead of the meaning "meeting/ convention", it'll shift to connote "height, pinnacle (of radio excellence)".
The design should have a modern, contemporary feel.
Target Market(s)
The main target audience is radio deejays, radio station management, marketers/ advertisers, journalists.

```html
<!DOCTYPE html>
<html lang="en">
<head>
<meta charset="utf-8">
<title>Wave Crestline</title>
<link href="https://fonts.googleapis.com/css2?family=Bodoni+Moda:opsz,wght@6..96,400&family=Gelasio:wght@400;700&family=Arimo:wght@400&display=swap" rel="stylesheet">
<style>
  :root {
    --ink: #000;
    --paper: #fff;
    --accent: #ffff00;
    --muted: #666;
    --rule: #999;
    --row: #dcdcdc;
    --row-text: #444;
    --display: "Bodoni Moda", "Didot", serif;
    --serif: "Gelasio", Georgia, serif;
    --sans: "Arimo", Arial, sans-serif;
  }
  html, body { margin: 0; padding: 0; overflow: hidden; }
  body { width: 1152px; height: 1200px; background: var(--paper); position: relative; font-family: var(--sans); color: var(--ink); }
  .abs { position: absolute; }

  .hero-art { left: 669px; top: 0; width: 483px; height: 658px;
    background: radial-gradient(ellipse at 30% 20%, #6a6a6a 0%, #9c9c9c 18%, #d6d6d6 42%, #f4f4f4 70%, #fff 100%); }
  .hero-veil { left: 669px; top: 172px; width: 360px; height: 70px; background: rgba(255,255,255,.75); }

  .brand { left: 123px; top: 84px; margin: 0; font-family: var(--display); font-weight: 400; font-size: 54px; letter-spacing: -2px; }

  .section-title { margin: 0; font-family: var(--display); font-weight: 400; font-size: 30px; letter-spacing: -1px; line-height: 1; }
  .section-rule { height: 1px; background: var(--rule); }

  .feature-photo { width: 384px; }
  .feature-tag { background: var(--accent); font-family: var(--display); font-size: 32px; letter-spacing: -1.4px; line-height: 53px; padding: 0 16px; white-space: nowrap; }
  .excerpt { font-size: 13.4px; line-height: 19px; color: var(--muted); margin: 0; }
  .share-bar { width: 384px; height: 29px; background: var(--ink); }
  .like { left: 3px; top: 3px; width: 45px; height: 21px; background: #eef1f7; border: 1px solid #9aa6c2; box-sizing: border-box; font-size: 10px; color: #3b5998; line-height: 19px; text-align: right; padding-right: 5px; }
  .like::before { content: ""; position: absolute; left: 5px; top: 5px; width: 8px; height: 8px; background: #3b5998; }
  .read-more { right: 11px; top: 6px; color: var(--accent); font-size: 13.4px; }

  .news-bar { width: 326px; height: 29px; background: var(--accent); font-family: var(--serif); font-size: 14.5px; line-height: 29px; }
  .news-bar .title { position: absolute; left: 11px; }
  .news-bar .date { position: absolute; right: 11px; font-size: 13px; }
  .news-photo { width: 154px; height: 115px; }
  .news-text { width: 150px; font-size: 11.5px; line-height: 14.4px; color: #333; margin: 0; }
  .news-link { font-size: 11.5px; color: var(--ink); text-decoration: underline; }

  .events { left: 874px; top: 260px; width: 154px; height: 498px; background: var(--ink); }
  .event-title { position: absolute; right: 11px; width: 140px; margin: 0; text-align: right; color: var(--paper); font-family: var(--serif); font-weight: 700; font-size: 15px; line-height: 15.5px; }
  .event-text { position: absolute; left: 11px; width: 124px; margin: 0; color: var(--accent); font-size: 11.5px; line-height: 14.4px; }

  .station { left: 528px; width: 499px; height: 29px; background: var(--row); font-family: var(--serif); font-size: 14px; color: var(--row-text); line-height: 29px; }
  .station .name { position: absolute; left: 12px; }
  .station .data { position: absolute; right: 17px; }

  .footer-rule { left: 125px; top: 1105px; width: 902px; }
  .footer { left: 125px; top: 1117px; width: 902px; margin: 0; text-align: center; font-family: var(--serif); font-size: 11.5px; color: #444; }
</style>
</head>
<body>
  <div class="abs hero-art" role="img" aria-label="Studio microphone photograph fading into white"></div>
  <div class="abs hero-veil"></div>

  <h1 class="abs brand">Wave Crestline</h1>

  <!-- Featured articles -->
  <h2 class="abs section-title" style="left:125px;top:200px;">Featured articles</h2>
  <div class="abs section-rule" style="left:125px;top:240px;width:384px;"></div>

  <div class="abs feature-photo" style="left:125px;top:260px;height:254px;background:linear-gradient(160deg,#f2f2f2 0%,#cfcfcf 55%,#9a9a9a 100%);" role="img" aria-label="Photograph of studio headphones"></div>
  <div class="abs feature-tag" style="left:125px;top:434px;">This is a title</div>
  <p class="abs excerpt" style="left:125px;top:524px;width:380px;">This is an excerpt. Lorem ipsum dolor sit amet, consectetur adipiscing elit. Quisque placerat dignissim purus, vitae auctor odio aliquam ut.</p>
  <div class="abs share-bar" style="left:125px;top:595px;">
    <span class="abs like">Like</span>
    <span class="abs read-more">Read more »</span>
  </div>

  <div class="abs feature-photo" style="left:125px;top:653px;height:259px;background:linear-gradient(180deg,#4d6f96 0%,#8fa6bf 45%,#d8dde2 75%,#a07a5a 100%);" role="img" aria-label="Photograph of a broadcast transmission tower against a cloudy sky"></div>
  <div class="abs feature-tag" style="left:125px;top:828px;">One more featured title</div>
  <p class="abs excerpt" style="left:125px;top:918px;width:380px;">This is an excerpt. Lorem ipsum dolor sit amet, consectetur adipiscing elit. Quisque placerat dignissim purus, vitae auctor odio aliquam ut.</p>
  <div class="abs share-bar" style="left:125px;top:989px;">
    <span class="abs like">Like</span>
    <span class="abs read-more" style="right:7px;">Read more »</span>
  </div>

  <!-- News -->
  <h2 class="abs section-title" style="left:528px;top:200px;">News</h2>
  <div class="abs section-rule" style="left:528px;top:240px;width:326px;"></div>

  <div class="abs news-bar" style="left:528px;top:259px;"><span class="title">First news title</span><span class="date">20/02/2011</span></div>
  <div class="abs news-photo" style="left:528px;top:298px;background:linear-gradient(160deg,#e4e0e6,#a49ca6 60%,#6f6672);" role="img" aria-label="Photograph of loudspeakers"></div>
  <p class="abs news-text" style="left:703px;top:297px;">This is an excerpt. Lorem ipsum dolor sit amet, consectetur adipiscing elit. Quisque placerat dignissim purus, vitae auctor odio aliquam ut.</p>
  <a class="abs news-link" style="left:704px;top:391px;">Read more »</a>

  <div class="abs news-bar" style="left:528px;top:441px;"><span class="title">Second news title</span><span class="date">20/02/2011</span></div>
  <div class="abs news-photo" style="left:528px;top:480px;background:linear-gradient(180deg,#1a1a1a 0%,#3a3a3a 50%,#a9c6d8 80%,#3a3a3a 100%);" role="img" aria-label="Illustration of a glowing audio equalizer"></div>
  <p class="abs news-text" style="left:703px;top:479px;">This is an excerpt. Lorem ipsum dolor sit amet, consectetur adipiscing elit. Quisque placerat dignissim purus, vitae auctor odio aliquam ut.</p>
  <a class="abs news-link" style="left:704px;top:573px;">Read more »</a>

  <div class="abs news-bar" style="left:528px;top:624px;"><span class="title">Third news title</span><span class="date">20/02/2011</span></div>
  <div class="abs news-photo" style="left:528px;top:662px;background:linear-gradient(135deg,#4a3320 0%,#9a6f3e 45%,#d6c9b5 65%,#3a2a1a 100%);" role="img" aria-label="Photograph of a studio microphone with pop filter"></div>
  <p class="abs news-text" style="left:703px;top:661px;">This is an excerpt. Lorem ipsum dolor sit amet, consectetur adipiscing elit. Quisque placerat dignissim purus, vitae auctor odio aliquam ut.</p>
  <a class="abs news-link" style="left:704px;top:755px;">Read more »</a>

  <!-- Events -->
  <h2 class="abs section-title" style="left:874px;top:200px;">Events</h2>
  <div class="abs section-rule" style="left:874px;top:240px;width:154px;"></div>
  <section class="abs events">
    <h3 class="event-title" style="top:20px;">Event Number One</h3>
    <p class="event-text" style="top:65px;">This is an excerpt. Lorem ipsum dolor sit amet, consectetur adipiscing elit. Quisque placerat dignissim purus, vitae auctor odio aliquam ut.</p>
    <h3 class="event-title" style="top:198px;">Another Event</h3>
    <p class="event-text" style="top:225px;">This is an excerpt. Lorem ipsum dolor sit amet, consectetur adipiscing elit.</p>
    <h3 class="event-title" style="top:318px;">One More Event Title</h3>
    <p class="event-text" style="top:356px;">This is an excerpt. Lorem ipsum dolor sit amet, consectetur adipiscing elit. Quisque placerat dignissim purus, vitae auctor odio aliquam ut.</p>
  </section>

  <!-- Radio Stations -->
  <h2 class="abs section-title" style="left:528px;top:802px;">Radio Stations</h2>
  <div class="abs section-rule" style="left:528px;top:842px;width:499px;"></div>
  <div class="abs station" style="top:854px;"><span class="name">Radio Station Number One</span><span class="data">Lorem ipsum data »</span></div>
  <div class="abs station" style="top:893px;"><span class="name">Radio Station Number Two</span><span class="data">Lorem ipsum data »</span></div>
  <div class="abs station" style="top:931px;"><span class="name">Another Radio Station</span><span class="data">Lorem ipsum data »</span></div>
  <div class="abs station" style="top:970px;"><span class="name">One more Radio Station</span><span class="data">Lorem ipsum data »</span></div>
  <div class="abs station" style="top:1008px;"><span class="name">The Last Radio Station</span><span class="data">Lorem ipsum data »</span></div>

  <!-- Footer -->
  <div class="abs section-rule footer-rule"></div>
  <p class="abs footer">© 2010 - Northgate Media. Website designed and developed by Pixel Forge. Credit to Dara Mwale for artwork.</p>
</body>
</html>
```